RW Stewardship real estate management company needs presentation folder to hand clients

looking for a folder with pockets that represent my real estate management company when i hand to client reports or promotional material. I only do resedential real estate. I want classy and professional - pictures or additioal graphixs are fine

when a client open i will usally insert text and reports about my business
also on the inside flap is usally place for my business card i will upload a picture so the theme can be constant

Target Market(s)

my existing real estate cleints
and i will use when i am soliciting new business

Industry/Entity Type

Real Estate

Font styles to use
Serif

Requirements
Must have
• must have logo
• must give appearance of professionalism and maturity
• have basic company info tel# ,address
• id like viewer to know I manage real estate - focus on residential small to large apartment buildings
• not strip malls, not giganic complexes - im a mid size company
• logo is black but i welcome color as u see fit
Nice to have
• maybe pictures
• my slogan - " we will manage your building like its our own "
• focus on professioanl, safe, trust worthy
• type style should be clear and readable - but im open to sugestions

```html
<!DOCTYPE html>
<html lang="en">
<head>
<meta charset="utf-8">
<title>RW Stewardship — Presentation Folder</title>
<link rel="stylesheet" href="https://fonts.googleapis.com/css2?family=Jost:wght@400;500&family=Arimo:wght@400;700&display=swap">
<style>
  :root {
    --canvas: #e4e4e4;
    --paper: #ffffff;
    --ink: #111111;
    --ink-soft: #3a3a3a;
    --skyline-faint: #dcdcdc;
    --skyline-dark: #0c0c0c;
    --crease: #e9e9e9;
    --pocket-edge: #cfcfcf;
  }
  * { box-sizing: border-box; margin: 0; padding: 0; }
  html, body { width: 1200px; height: 1200px; overflow: hidden; }
  body { background: var(--canvas); position: relative; font-family: "Jost", sans-serif; color: var(--ink); }

  .spread { position: absolute; left: 220px; width: 760px; height: 500px; display: flex; box-shadow: 0 10px 28px rgba(0,0,0,.18); }
  .spread--outside { top: 50px; }
  .spread--inside { top: 600px; }
  .panel { position: relative; width: 380px; height: 500px; background: var(--paper); overflow: hidden; }
  .panel + .panel { border-left: 1px solid var(--crease); }

  .brand { display: flex; align-items: center; gap: 8px; justify-content: center; font-family: "Jost", sans-serif; font-weight: 500; color: var(--ink); letter-spacing: .04em; text-transform: uppercase; }
  .brand__mark { background: var(--ink); flex: none; }

  /* outside front */
  .front .brand { margin-top: 62px; font-size: 22px; }
  .front .brand__mark { width: 14px; height: 14px; }
  .slogan { margin-top: 16px; text-align: center; font-size: 17px; line-height: 1.3; color: var(--ink-soft); }
  .skyline { position: absolute; left: 0; right: 0; bottom: 0; }
  .front .skyline { height: 100px; background: linear-gradient(to top, var(--skyline-dark) 0%, #1c1c1c 100%); }
  .back .skyline { height: 100px; background: linear-gradient(to right, var(--skyline-faint) 0%, var(--skyline-faint) 80%, #2a2a2a 90%, var(--skyline-dark) 100%); }

  .contact { position: absolute; left: 24px; bottom: 20px; font-family: "Arimo", sans-serif; font-size: 9px; color: var(--ink-soft); line-height: 1.5; white-space: nowrap; }
  .contact .brand { justify-content: flex-start; font-size: 11px; margin-bottom: 6px; }
  .contact .brand__mark { width: 8px; height: 8px; }
  .contact__row span + span { margin-left: 8px; }

  /* inside */
  .pocket { position: absolute; left: 0; right: 0; bottom: 0; height: 165px; background: var(--paper); border-top: 1px solid var(--pocket-edge); box-shadow: 0 -6px 12px rgba(0,0,0,.06); }
  .pocket--left { border-top-right-radius: 30px 14px; border-right: 1px solid var(--pocket-edge); }
  .pocket--right { border-top-left-radius: 30px 14px; border-left: 1px solid var(--pocket-edge); }
  .flap { position: absolute; top: 20px; bottom: 165px; width: 14px; border: 1px solid var(--crease); }
  .flap--left { left: 12px; }
  .flap--right { right: 12px; }
  .notch { position: absolute; top: 200px; }
  .notch--left { left: 12px; }
  .notch--right { right: 12px; }
  .pocket--left .brand { margin-top: 68px; font-size: 18px; }
  .pocket--left .brand__mark { width: 12px; height: 12px; }

  .card-slot { position: absolute; left: 118px; top: 40px; width: 176px; height: 92px; }
  .card { position: absolute; inset: 6px; border: 1px solid #888; background: var(--paper); display: flex; padding: 10px 8px 6px; gap: 8px; font-family: "Arimo", sans-serif; }
  .card__brand { width: 58px; border-right: 1px solid var(--ink); display: flex; flex-direction: column; align-items: center; justify-content: center; gap: 4px; font-family: "Jost", sans-serif; font-weight: 500; font-size: 7px; text-transform: uppercase; text-align: center; line-height: 1.1; }
  .card__brand i { width: 8px; height: 8px; background: var(--ink); display: block; }
  .card__name { font-weight: 700; font-size: 11px; }
  .card__title { font-size: 5px; letter-spacing: .05em; text-transform: uppercase; margin-bottom: 5px; }
  .card__line { font-size: 5.5px; line-height: 1.4; color: var(--ink-soft); }
  .card__slogan { position: absolute; left: 8px; bottom: 3px; font-size: 4.5px; text-transform: uppercase; letter-spacing: .04em; }
  .slit { position: absolute; width: 18px; height: 2px; background: var(--ink); }
  .slit--tl { left: -2px; top: 8px; transform: rotate(-45deg); }
  .slit--bl { left: -2px; bottom: 8px; transform: rotate(45deg); }
  .slit--tr { right: -2px; top: 8px; transform: rotate(45deg); }
  .slit--br { right: -2px; bottom: 8px; transform: rotate(-45deg); }
</style>
</head>
<body>

<section class="spread spread--outside">
  <div class="panel back">
    <div class="skyline" role="img" aria-label="City skyline silhouette in light grey, turning black toward the spine"></div>
    <div class="contact">
      <div class="brand"><span class="brand__mark"></span>RW Stewardship</div>
      <div class="contact__row"><span>(000) 555-0142</span><span>(000) 555-0143</span><span>hello@rwstewardship.com</span></div>
      <div class="contact__row"><span>Suite 210, 48 Elm Row</span><span>Fairview NY 10522</span></div>
    </div>
  </div>
  <div class="panel front">
    <div class="brand"><span class="brand__mark"></span>RW Stewardship</div>
    <p class="slogan">We Will Manage Your Building<br>Like Its Our Own</p>
    <div class="skyline" role="img" aria-label="Black city skyline silhouette of apartment towers"></div>
  </div>
</section>

<section class="spread spread--inside">
  <div class="panel">
    <div class="flap flap--left"></div>
    <svg class="notch notch--left" width="30" height="40" viewBox="0 0 30 40"><path d="M1 0 A18 20 0 0 1 1 40" fill="none" stroke="#cfcfcf"/></svg>
    <div class="pocket pocket--left">
      <div class="brand"><span class="brand__mark"></span>RW Stewardship</div>
    </div>
  </div>
  <div class="panel">
    <div class="flap flap--right"></div>
    <svg class="notch notch--right" width="30" height="40" viewBox="0 0 30 40"><path d="M29 0 A18 20 0 0 0 29 40" fill="none" stroke="#cfcfcf"/></svg>
    <div class="pocket pocket--right">
      <div class="card-slot">
        <span class="slit slit--tl"></span><span class="slit slit--bl"></span>
        <span class="slit slit--tr"></span><span class="slit slit--br"></span>
        <div class="card">
          <div class="card__brand"><i></i>RW Stewardship</div>
          <div>
            <div class="card__name">Daniel Hart</div>
            <div class="card__title">Master Building Manager</div>
            <div class="card__line">office 314-555-0190</div>
            <div class="card__line">email dhart@rwstewardship.com</div>
            <div class="card__line">cell 314-555-0177</div>
          </div>
          <div class="card__slogan">We will manage your building like its our own</div>
        </div>
      </div>
    </div>
  </div>
</section>

</body>
</html>
```